Letterhead Design Project

Our firm recently came out with a new logo and new website and we would like to design letterhead that makes use of the new look.

Our firm is an energy consulting firm. We help our customers find ways to spend less money on their energy expenses (we cater to commercial and industrial accounts) by helping them find a lower rate for every unit of energy they consume, install more energy efficient measures so that they end up using fewer units of energy or determine if making the energy themselves can be done more cost effectively

Industry/Entity Type

Industrial

Requirements
Must have
• Must have our logo
must have our contact information
Nice to have
• some sort of watermark

```html
<!DOCTYPE html>
<html lang="en">
<head>
<meta charset="utf-8">
<title>Lumenarc Energy Letterhead</title>
<link href="https://fonts.googleapis.com/css2?family=Questrial&family=Source+Sans+3:wght@400;600&display=swap" rel="stylesheet">
<style>
  :root {
    --stage: #4f4f4f;
    --paper: #ffffff;
    --ink: #3a3a3c;
    --muted: #6d6e70;
    --teal: #2a8aa0;
    --wash: #eef0f2;
  }
  html, body {
    margin: 0;
    padding: 0;
    width: 1200px;
    height: 891px;
    overflow: hidden;
    background: var(--stage);
  }
  .letterhead {
    position: absolute;
    left: 205px;
    top: 61px;
    width: 612px;
    height: 791px;
    background: var(--paper);
    overflow: hidden;
  }
  .brand {
    position: absolute;
    left: 40px;
    top: 70px;
    display: flex;
    align-items: center;
    gap: 10px;
  }
  .brand-square {
    width: 14px;
    height: 14px;
    background: var(--ink);
  }
  .brand-name {
    font-family: "Questrial", sans-serif;
    font-size: 22px;
    letter-spacing: 6px;
    color: var(--ink);
    line-height: 1;
  }
  .contact {
    position: absolute;
    left: 462px;
    top: 44px;
    height: 64px;
    border-left: 2px solid var(--teal);
    padding-left: 17px;
    font-family: "Source Sans 3", sans-serif;
    font-size: 9.5px;
    color: var(--muted);
    line-height: 13px;
  }
  .contact-address { margin: 2px 0 6px; }
  .contact-line { margin: 0; }
  .contact-label {
    display: inline-block;
    width: 26px;
    font-weight: 600;
    color: var(--teal);
  }
  .watermark {
    position: absolute;
    left: 0;
    bottom: 0;
    width: 612px;
    height: 380px;
    background: linear-gradient(170deg, rgba(238,240,242,0) 30%, var(--wash) 100%);
  }
  .website {
    position: absolute;
    right: 27px;
    bottom: 20px;
    font-family: "Source Sans 3", sans-serif;
    font-size: 10.5px;
    color: var(--teal);
    margin: 0;
  }
</style>
</head>
<body>
  <main class="letterhead">
    <div class="watermark" role="img" aria-label="Faint brand watermark"></div>
    <header class="brand">
      <span class="brand-square"></span>
      <span class="brand-name">LUMENARC</span>
    </header>
    <address class="contact" style="font-style:normal">
      <p class="contact-address">218 Alder Row Kingsford,<br>ON Canada K2P4R8</p>
      <p class="contact-line"><span class="contact-label">Telp.</span> 555-218-4406</p>
      <p class="contact-line"><span class="contact-label">Fax.</span> 555-218-4407</p>
    </address>
    <p class="website">www.lumenarcenergy.com</p>
  </main>
</body>
</html>
```